Pro-Athlete Founded Charity Seeks Letterhead Design

A non-profit organization, called Lanterns for "Discovery: The Mark Tilden Foundation," was founded by an PGL athelete to help children born with cardiac heart defects. The charity funds this initiative under the name, "The Kindred Mile."

Please create a letterhead considering the following requirements:

- Use Dominant logo: The Kindred Mile

- Use Auxillary logo: Lanterns for Discovery

- Address:2407 North Meridian Parkway Third Floor, Boca Raton, FL 33419

- Website: www.lanternsfordiscovery-demo.org

- Editable places for date; letter recipients' name/address; signature block

- Coloring: Dakota Falcons blue/black (athlete plays for that PGL team); and red (for cardiology/heart disease)... reference logos

Thanks to any and all designers who work on this project! A winner WILL be selected, and follow-on projects will be requested of the winning designer.

Industry/Entity Type

Non-Profit

```html
<!DOCTYPE html>
<html lang="en">
<head>
<meta charset="utf-8">
<title>Lanterns for Discovery Letterhead</title>
<link rel="stylesheet" href="https://fonts.googleapis.com/css2?family=Lato:wght@400;700;900&display=swap">
<style>
  :root {
    --brand-red: #c8202f;
    --ink: #1f1f1f;
    --body-ink: #333333;
    --rule: #2a2a2a;
    --page: #ffffff;
    --page-edge: #9a9a9a;
    --mark-tint: rgba(120, 170, 210, 0.12);
  }
  html, body {
    margin: 0;
    padding: 0;
    width: 929px;
    height: 1200px;
    overflow: hidden;
    background: var(--page);
  }
  .letterhead {
    position: relative;
    width: 929px;
    height: 1200px;
    box-sizing: border-box;
    border: 1px solid var(--page-edge);
    background: var(--page);
    font-family: "Lato", Arial, sans-serif;
    color: var(--body-ink);
    overflow: hidden;
  }
  .brand-mark {
    position: absolute;
    left: 40px;
    top: 42px;
    width: 130px;
    display: flex;
    flex-direction: column;
    align-items: center;
    gap: 8px;
  }
  .brand-mark__dot {
    width: 46px;
    height: 46px;
    border-radius: 50%;
    background: var(--brand-red);
  }
  .brand-mark__name {
    font-weight: 700;
    font-size: 17px;
    line-height: 1.2;
    color: var(--brand-red);
    text-align: center;
  }
  .header-rule {
    position: absolute;
    left: 183px;
    top: 34px;
    width: 3px;
    height: 124px;
    background: var(--rule);
  }
  .org-block {
    position: absolute;
    left: 205px;
    top: 62px;
    width: 560px;
    text-align: center;
  }
  .org-block__name {
    margin: 0;
    font-size: 20.5px;
    font-weight: 700;
    color: var(--brand-red);
    letter-spacing: 0.2px;
  }
  .org-block__address,
  .org-block__web {
    margin: 2px 0 0;
    font-size: 17px;
    font-weight: 700;
    color: var(--ink);
  }
  .faint-mark {
    position: absolute;
    left: 300px;
    top: 445px;
    width: 340px;
    height: 340px;
    border-radius: 50%;
    background: var(--mark-tint);
  }
  .letter-body {
    position: absolute;
    left: 43px;
    top: 236px;
    width: 852px;
    font-size: 15.6px;
    line-height: 19.7px;
  }
  .letter-body p { margin: 0; }
  .letter-date { margin-bottom: 55px !important; }
  .recipient { margin-bottom: 54px !important; }
  .salutation { margin-bottom: 15px !important; }
  .letter-paragraph { margin-bottom: 18px !important; }
  .closing { margin-bottom: 65px !important; }
</style>
</head>
<body>
  <main class="letterhead">
    <div class="brand-mark">
      <span class="brand-mark__dot"></span>
      <span class="brand-mark__name">The Kindred<br>Mile</span>
    </div>

    <div class="header-rule"></div>

    <header class="org-block">
      <h1 class="org-block__name">Lanterns for Discovery: The Corwin Ashvale Foundation</h1>
      <p class="org-block__address">2407 North Meridian Parkway | Third Floor | Harbor Vale, FL 33419</p>
      <p class="org-block__web">www.lanternsfordiscovery-demo.org</p>
    </header>

    <div class="faint-mark" aria-hidden="true"></div>

    <section class="letter-body">
      <p class="letter-date">[Insert Date]</p>

      <p class="recipient">[Recipient]<br>[Title]<br>[Company]<br>[Address 1]<br>[Address 2]<br>[Address 3]</p>

      <p class="salutation">Dear [Recipient]:</p>

      <p class="letter-paragraph">Fusce neque mi, consectetuer gravida, convallis ac, varius a, pede. Fusce pellentesque pretium quam. Ut luctus, justo id volutpat iaculis, est diam pulvinar sem, quis bibendum turpis dui eget mauris. Sed in mauris. Ut massa. Pellentesque condimentum felis nec sapien. Integer posuere elit at turpis. Nulla facilisi. Sed sapien ipsum, commodo ut, facilisis vitae, ultrices non, metus. Aenean non nulla. Curabitur molestie volutpat magna. Vestibulum tempor faucibus nisi. Pellentesque vitae enim.</p>

      <p class="letter-paragraph">Aliquam rhoncus volutpat mauris. Sed auctor. Donec tincidunt velit et tellus. Donec sed augue eget lacus placerat adipiscing. Ut convallis suscipit nulla. Morbi posuere ullamcorper ligula. Duis sit amet odio nec lorem ornare gravida. Suspendisse ante nulla, gravida quis, eleifend sit amet, placerat eget, purus. Sed egestas magna ut erat. Vivamus euismod, odio id mattis porttitor, tellus nisl consectetuer turpis, ut auctor enim justo euismod nulla. Fusce eget diam vulputate massa tempor tempor.</p>

      <p class="letter-paragraph">In ante. Phasellus convallis, nisl in vestibulum facilisis, lacus pede bibendum urna, dapibus pellentesque eros magna sed nibh. Etiam tortor arcu, porta nec, laoreet quis, mollis in, libero. Aenean dapibus est a metus. In sit amet elit. Pellentesque luctus lacus scelerisque arcu. Cras mattis diam. Sed molestie, lectus id bibendum luctus, magna orci luctus quam, et auctor urna diam sit amet ligula. Sed purus dui, suscipit et, malesuada non, consectetuer in, augue. Proin et sapien. Maecenas aliquam, nibh id aliquet tincidunt, ante neque pulvinar mauris, sit amet fermentum nibh augue mollis risus. Mauris porttitor varius mauris. Vivamus in urna et sem accumsan imperdiet. Aenean fringilla, eros tincidunt gravida elementum, justo eros pharetra felis, in rhoncus arcu lectus non enim. Phasellus odio tortor, mattis ut, mattis elementum, luctus at, orci.</p>

      <p class="closing">Sincerely,</p>

      <p class="signature">Name<br>[Your Title]</p>
    </section>
  </main>
</body>
</html>
```